Redesign wellness clinic website

The project is redesign a wellness clinic http://www.thornleighvitality.example. The new website is to be responsive,clean,bright and a strong call to action which is to book an appointment. The logo will remain the same but the colour scheme on the website should be reflect purple white and green. I want it to be bright and cheerful and the feeling of clarity. The website shouldn't be overloaded with content but more visuals.

Target Market(s)

Anyone that has corporate wellness benefits within the downtown Toronto core. Majority of audience are professional working in Media, Telecommunications and Investments.

Industry/Entity Type

Health And Wellness

Number of Pages Required

5+ page

Font styles to use
Sans Serif

Colors
ffffff
886aae
acd036

Requirements
Must have
• -Strong call to action which is book an appointment like this page https://www.kestrelmotion.example/
• -Services provided icons on the page like https://www.brightpathvitalityhouse.example/
• - Pictures of a good visualizing a fit and healthy life
• - Strong ratings from Quorva, Zintrel, PostMaz, similar to this website http://www.summitbalancehealth.example/our-team-professionals/
• - Bright and clear
Should not have
• -No black and white images (redo our pictures)
• -Dark themes

```html
<!DOCTYPE html>
<html lang="en">
<head>
<meta charset="utf-8">
<title>Thornleigh Vitality Centre</title>
<link href="https://fonts.googleapis.com/css2?family=Lato:ital,wght@0,400;0,700;1,400&display=swap" rel="stylesheet">
<style>
:root{
  --purple:#886aae;
  --purple-deep:#6f4f9c;
  --green:#acd036;
  --green-deep:#94bb22;
  --white:#ffffff;
  --ink:#333333;
  --muted:#555555;
  --dark:#4a3f38;
}
*{box-sizing:border-box;margin:0;padding:0}
html,body{width:1200px;height:3114px;overflow:hidden;background:var(--white)}
body{position:relative;font-family:'Lato',sans-serif;color:var(--ink)}
.abs{position:absolute}

/* header */
.site-header{position:absolute;left:0;top:0;width:1200px;height:114px;background:var(--white)}
.brand{position:absolute;left:84px;top:20px;display:flex;align-items:center;gap:16px}
.brand-mark{width:110px;height:110px;border-radius:50%;background:var(--white);border:6px solid var(--green);box-shadow:0 2px 6px rgba(0,0,0,.15)}
.brand-name{font-size:25px;font-weight:700;color:var(--purple-deep);line-height:1.15}
.phone{position:absolute;right:88px;top:16px;font-size:21px;color:var(--ink);display:flex;align-items:center;gap:6px}
.main-nav{position:absolute;right:88px;top:60px;display:flex;gap:30px;font-size:17px;color:var(--muted)}
.main-nav .active{color:var(--purple-deep);font-weight:700}

/* hero */
.hero{position:absolute;left:0;top:114px;width:1200px;height:602px;background:linear-gradient(100deg,#ece9e6 0%,#e2d8cf 45%,#c9a98e 70%,#e4d3c4 100%)}
.hero-title{position:absolute;left:104px;top:142px}
.hero-title .pre{display:block;font-size:42px;color:var(--green);line-height:1.2}
.hero-title .main{display:block;font-size:42px;color:var(--ink);line-height:1.2}
.hero-text{position:absolute;left:104px;top:252px;width:410px;font-size:16px;line-height:1.55;color:var(--muted)}
.btn-book{position:absolute;left:104px;top:320px;width:276px;height:60px;border:2px solid var(--purple-deep);background:rgba(255,255,255,.55);color:var(--purple-deep);font-size:21px;display:flex;align-items:center;justify-content:center}
.hero-dots{position:absolute;left:555px;top:478px;display:flex;gap:8px}
.hero-dots span{width:14px;height:14px;border-radius:50%;background:#444}
.hero-dots span:first-child{background:transparent;border:2px solid #444}
.hero-curve{position:absolute;left:0;top:500px}

/* about */
.about-photo{position:absolute;left:106px;top:739px;width:446px;height:293px;background:linear-gradient(135deg,#f2f0f2,#d6d2d8);border:1px solid #ccc}
.section-title{font-size:35px;font-weight:400;color:var(--ink)}
.about-title{position:absolute;left:598px;top:740px}
.about-text{position:absolute;left:598px;top:800px;width:540px;font-size:16px;line-height:1.95;color:var(--muted)}
.btn-outline{position:absolute;display:flex;align-items:center;justify-content:center;border:2px solid var(--purple-deep);color:var(--purple-deep);font-size:16px}
.btn-learn{left:598px;top:980px;width:174px;height:44px}

/* services */
.services{position:absolute;left:0;top:1127px;width:1200px;height:457px;background:linear-gradient(180deg,#7d5ca8,#8a6cb1 60%,#7b5aa6)}
.services-badge{position:absolute;left:560px;top:1090px;width:80px;height:80px;border-radius:50%;background:var(--white);border:6px solid var(--green)}
.services-title{position:absolute;left:0;top:1176px;width:1200px;text-align:center;font-size:32px;color:var(--white)}
.service{position:absolute;top:1246px;width:220px;text-align:center;color:var(--white)}
.service-icon{width:116px;height:116px;margin:0 auto;border-radius:50%;border:3px solid var(--white);padding:6px}
.service-icon .disc{width:100%;height:100%;border-radius:50%;background:var(--green);display:flex;align-items:center;justify-content:center}
.service h3{margin-top:14px;font-size:18px;font-weight:700;letter-spacing:.3px}
.service p{margin-top:8px;font-size:11.5px;line-height:1.6;opacity:.9}
.btn-more{left:507px;top:1503px;width:196px;height:42px;border:2px solid var(--white);color:var(--white);font-size:15px}

/* blog */
.blog-title{position:absolute;left:89px;top:1640px;font-size:32px}
.blog-photo{position:absolute;width:202px;height:202px;border-radius:50%}
.blog-photo.one{left:80px;top:1716px;background:linear-gradient(135deg,#d8c6b6,#3e6fb3)}
.blog-photo.two{left:609px;top:1711px;background:linear-gradient(135deg,#cfa585,#efe5dc)}
.blog-post{position:absolute;width:270px}
.blog-post h4{font-size:20px;font-weight:700;color:var(--purple-deep);line-height:1.4}
.blog-post p{margin-top:14px;font-size:17px;line-height:1.55;color:var(--muted)}
.blog-post .read{display:block;margin-top:14px;font-size:17px;color:var(--ink)}

/* testimonial */
.testimonial{position:absolute;left:0;top:1993px;width:1200px;height:380px;background:linear-gradient(90deg,#3f3630,#5a4b40 50%,#3f3630)}
.testimonial h2{position:absolute;left:0;top:60px;width:1200px;text-align:center;font-size:28px;font-weight:400;color:var(--white)}
.quote-mark{position:absolute;left:0;top:110px;width:1200px;text-align:center;font-size:70px;font-weight:700;color:var(--white);line-height:1}
.quote-text{position:absolute;left:220px;top:176px;width:760px;text-align:center;font-size:19px;font-style:italic;line-height:1.75;color:#e8e2dc}
.quote-author{position:absolute;left:0;top:262px;width:1200px;text-align:center;font-size:19px;color:var(--white)}
.arrow{position:absolute;top:2152px}

/* ratings */
.rating{position:absolute;top:2433px;width:204px;height:135px}
.rating.zintrel{left:255px;background:#f4f7f0;border:1px solid #9cc36a}
.rating.quorva{left:500px;background:#fbf1f1;border:1px solid #c0392b}
.rating.postmaz{left:743px;background:#e8141e}

/* footer */
.site-footer{position:absolute;left:0;top:2653px;width:1200px;height:461px;background:var(--green)}
.foot-col{position:absolute;top:2710px;color:var(--white)}
.foot-col h5{font-size:18px;font-weight:700;margin-bottom:14px;letter-spacing:.3px}
.foot-col li{list-style:none;font-size:16px;line-height:31px}
.foot-col.contact li{font-size:14.5px}
.foot-rule{position:absolute;left:84px;width:1032px;height:1px;background:rgba(255,255,255,.7)}
.hours-label{position:absolute;left:128px;top:2976px;font-size:19px;color:var(--white)}
.hours{position:absolute;top:2968px;font-size:14.5px;line-height:1.45;color:var(--white)}
.follow{position:absolute;left:780px;top:2979px;font-size:18px;color:var(--white)}
.socials{position:absolute;left:902px;top:2970px;display:flex;gap:10px}
.socials span{width:38px;height:38px;border-radius:50%;border:2px solid var(--white)}
.copyright{position:absolute;left:0;top:3067px;width:1200px;text-align:center;font-size:13px;color:var(--white)}
</style>
</head>
<body>

<header class="site-header">
  <div class="brand">
    <div class="brand-mark"></div>
    <div class="brand-name">Thornleigh<br>Vitality Centre</div>
  </div>
  <div class="phone">
    <svg width="22" height="22" viewBox="0 0 24 24"><path fill="#94bb22" d="M6.6 10.8a15.1 15.1 0 0 0 6.6 6.6l2.2-2.2a1 1 0 0 1 1-.25 11.4 11.4 0 0 0 3.6.57 1 1 0 0 1 1 1V20a1 1 0 0 1-1 1A17 17 0 0 1 3 4a1 1 0 0 1 1-1h3.5a1 1 0 0 1 1 1c0 1.25.2 2.45.57 3.57a1 1 0 0 1-.25 1z"/></svg>
    416 555 0182
  </div>
  <nav class="main-nav">
    <span class="active">Home</span><span>Fees &amp; Services</span><span>Our Staff</span><span>News &amp; Updates</span><span>Corporate Wellness</span><span>Contact</span>
  </nav>
</header>

<section class="hero" role="img" aria-label="Woman relaxing face down on a massage table during a back massage">
</section>
<div class="hero-title abs" style="position:absolute;left:104px;top:256px">
  <span style="display:block;font-size:42px;color:var(--green);line-height:1.2">Welcome to</span>
  <span style="display:block;font-size:42px;color:var(--ink);line-height:1.2">Thornleigh Vitality Centre</span>
</div>
<p class="hero-text" style="top:366px">Vivamus porttitor purus nisi eleifend libero a tempus libero lectus feugiat felis vlacus Ut ac mi quis</p>
<div class="btn-book" style="top:434px">Book an Appointment</div>
<div class="hero-dots" style="top:592px"><span></span><span></span><span></span><span></span></div>
<svg class="hero-curve" style="top:610px" width="1200" height="110" viewBox="0 0 1200 110">
  <path d="M0 110 L0 80 Q600 -20 1200 100 L1200 110 Z" fill="#ffffff"/>
  <path d="M60 80 Q600 0 1200 100" fill="none" stroke="#94bb22" stroke-width="5"/>
</svg>

<div class="about-photo" role="img" aria-label="Physiotherapist treating a patient lying on a treatment table"></div>
<h2 class="section-title about-title">Little About Our Centre</h2>
<p class="about-text">Established in 1989 the Thornleigh Vitality Centre has become one of Canada's leaders in providing quality care and innovative wellness programs for the community. The founder and director Dr. Colin Marwick's vision has come to life with over 30 practitioners providing a multitude of different services under one roof.</p>
<div class="btn-outline btn-learn">Learn More</div>

<section class="services"></section>
<div class="services-badge"></div>
<h2 class="services-title">Our Services</h2>

<div class="service" style="left:50px">
  <div class="service-icon"><div class="disc">
    <svg width="56" height="56" viewBox="0 0 56 56" fill="#fff"><rect x="20" y="4" width="16" height="8" rx="3"/><rect x="18" y="15" width="20" height="8" rx="3"/><rect x="17" y="26" width="22" height="8" rx="3"/><rect x="18" y="37" width="20" height="8" rx="3"/><rect x="21" y="48" width="14" height="6" rx="3"/></svg>
  </div></div>
  <h3>CHIROPRACTIC</h3>
  <p>Chiropractic is a non-invasive, hands-on health care discipline that focuses on treatment</p>
</div>
<div class="service" style="left:268px">
  <div class="service-icon"><div class="disc">
    <svg width="56" height="56" viewBox="0 0 56 56" fill="#fff"><rect x="6" y="34" width="44" height="6" rx="2"/><rect x="10" y="40" width="4" height="10"/><rect x="42" y="40" width="4" height="10"/><rect x="24" y="8" width="8" height="22" rx="2"/><rect x="17" y="15" width="22" height="8" rx="2"/></svg>
  </div></div>
  <h3>PHYSIOTHERAPY</h3>
  <p>Physiotherapy is a drug-free health care practice. Physiotherapists work in partnership</p>
</div>
<div class="service" style="left:488px">
  <div class="service-icon"><div class="disc">
    <svg width="56" height="56" viewBox="0 0 56 56" fill="none" stroke="#fff" stroke-width="4"><circle cx="28" cy="28" r="20"/><circle cx="28" cy="28" r="10"/><circle cx="28" cy="28" r="2" fill="#fff"/></svg>
  </div></div>
  <h3>PERSONAL TRAINING</h3>
  <p>The personal training aspect at Thornleigh Vitality Centre is one that most people will not be</p>
</div>
<div class="service" style="left:714px">
  <div class="service-icon"><div class="disc">
    <svg width="56" height="56" viewBox="0 0 56 56" fill="#fff"><ellipse cx="28" cy="12" rx="10" ry="6"/><ellipse cx="28" cy="26" rx="15" ry="6"/><ellipse cx="28" cy="42" rx="21" ry="8"/></svg>
  </div></div>
  <h3>MASSAGE THERAPY</h3>
  <p>Swedish Massage<br>Hot Stone Massage<br>Sports Massage</p>
</div>
<div class="service" style="left:924px">
  <div class="service-icon"><div class="disc">
    <svg width="56" height="56" viewBox="0 0 56 56" fill="none" stroke="#fff" stroke-width="3"><ellipse cx="28" cy="15" rx="7" ry="11"/><ellipse cx="28" cy="41" rx="7" ry="11"/><ellipse cx="15" cy="28" rx="11" ry="7"/><ellipse cx="41" cy="28" rx="11" ry="7"/><circle cx="28" cy="28" r="4" fill="#fff"/></svg>
  </div></div>
  <h3>OSTEOPATHY</h3>
  <p>Osteopathy is patient-centered treatment that enhances the body's natural ability</p>
</div>
<div class="btn-outline btn-more">View More Services</div>

<h2 class="section-title blog-title">From Our Blogs</h2>
<div class="blog-photo one" role="img" aria-label="Senior man in a blue shirt receiving a shoulder assessment"></div>
<article class="blog-post" style="left:301px;top:1726px">
  <h4>Vivamus porttitor purus nisi eleifend liber</h4>
  <p>mollis aliquam Curabitur iaculis tempus eros Curabitur vel mi sit amet magna a tempus libero</p>
  <span class="read">READ MORE</span>
</article>
<div class="blog-photo two" role="img" aria-label="Woman relaxing during a spa massage"></div>
<article class="blog-post" style="left:830px;top:1722px">
  <h4>Etiam eu urna Sed porta Suspendisse quam</h4>
  <p>mollis aliquam Curabitur iaculis tempus eros Curabitur vel mi sit amet magna a tempus libero</p>
  <span class="read">READ MORE</span>
</article>

<section class="testimonial" role="img" aria-label="Softly blurred treatment room in warm brown tones">
  <h2>What Our Patient Says</h2>
  <div class="quote-mark">&ldquo;</div>
  <p class="quote-text">Morbi diam mauris viverra in gravida eu mattis in ante Morbi eget arcu Morbi porta libero id ullamcorper nonummy nibh ligula pulvinar metus eget</p>
  <p class="quote-author">By Author Name</p>
</section>
<svg class="arrow" style="left:148px" width="28" height="62" viewBox="0 0 28 62"><path d="M24 2 L4 31 L24 60" fill="none" stroke="#fff" stroke-width="3"/></svg>
<svg class="arrow" style="left:1018px" width="28" height="62" viewBox="0 0 28 62"><path d="M4 2 L24 31 L4 60" fill="none" stroke="#fff" stroke-width="3"/></svg>

<div class="rating zintrel" role="img" aria-label="Zintrel five star review badge"></div>
<div class="rating quorva" role="img" aria-label="Quorva five star rating badge"></div>
<div class="rating postmaz" role="img" aria-label="PostMaz five star rating badge"></div>

<footer class="site-footer"></footer>
<ul class="foot-col" style="left:139px"><h5>OUR CENTRE</h5><li>About Us</li><li>Why Us</li><li>Our Patients</li><li>Blogs</li><li>News</li></ul>
<ul class="foot-col" style="left:388px"><h5>SERVICES</h5><li>Chiropractic</li><li>Physiotherapy</li><li>Active Rehabilitation</li><li>Massage Therapy</li><li>Osteopathy</li></ul>
<ul class="foot-col" style="left:650px"><h5>RESOURCES</h5><li>Our Staff</li><li>Fees</li><li>Form</li><li>Corporate Wellness</li><li>Contact</li></ul>
<ul class="foot-col contact" style="left:878px"><h5>CONTACT US</h5><li>48 Alder Lane East, Suite 210</li><li>Toronto, Ontario M0X 2K5</li><li>Phone: 416-555-0182</li><li>Fax: 416-555-0187</li></ul>
<div class="foot-rule" style="top:2956px"></div>
<div class="hours-label">Hours of Opening</div>
<div class="hours" style="left:337px">Monday - Friday<br>7:30am - 8pm</div>
<div class="hours" style="left:497px;top:2976px">Saturday 10am - 5pm<br>Sunday 10am - 5pm</div>
<div class="follow">Follow Us</div>
<div class="socials"><span></span><span></span><span></span><span></span></div>
<div class="foot-rule" style="top:3035px"></div>
<p class="copyright">&copy; 2017 Company Name All right reserved</p>

</body>
</html>
```